label update for bottle change

The goal is to adapt the label's design and shape to the new bottle, maintaining its defining elements such as the font, vertical name, company logo, background pattern, and color. The new design should not be identical to the old one, but rather an evolution of it. The gold stripe on the bottom is not mandatory, but the writing "BORGO DEL MONTE / EST. 1886" must be retained, slightly enlarged.

The font name is: Brandon Text

```html
<!DOCTYPE html>
<html lang="it">
<head>
<meta charset="utf-8">
<title>Amaro di Carattere – Carciofo label</title>
<link href="https://fonts.googleapis.com/css2?family=Josefin+Sans:wght@400;600;700&display=swap" rel="stylesheet">
<style>
  :root {
    --label-purple: #440754;
    --label-gold: #a3883a;
    --text-white: #ffffff;
    --sketch-lilac: #8a55a8;
    --page-bg: #ffffff;
  }
  html, body {
    margin: 0;
    padding: 0;
    width: 1200px;
    height: 1200px;
    overflow: hidden;
    background: var(--page-bg);
  }
  .canvas {
    position: relative;
    width: 1200px;
    height: 1200px;
  }
  .label {
    position: absolute;
    left: 209px;
    top: 63px;
    width: 782px;
    height: 1073px;
  }
  .label-body { fill: var(--label-purple); }
  .label-band { fill: var(--label-gold); }
  .label-frame {
    fill: none;
    stroke: var(--label-gold);
    stroke-width: 1.6;
  }
  .label-outline {
    fill: none;
    stroke: var(--label-purple);
    stroke-width: 1.2;
  }
  .text-maker {
    font-family: "Josefin Sans", sans-serif;
    font-weight: 600;
    font-size: 19px;
    letter-spacing: 7px;
    fill: var(--text-white);
  }
  .text-brand {
    font-family: "Josefin Sans", sans-serif;
    font-weight: 700;
    font-size: 44px;
    fill: var(--text-white);
  }
  .text-product {
    font-family: "Josefin Sans", sans-serif;
    font-weight: 700;
    font-size: 112px;
    fill: var(--text-white);
  }
  .text-tagline {
    font-family: "Josefin Sans", sans-serif;
    font-weight: 400;
    font-size: 37px;
    fill: var(--label-gold);
  }
  .text-origin {
    font-family: "Josefin Sans", sans-serif;
    font-weight: 700;
    font-size: 19px;
    letter-spacing: 1.5px;
    fill: var(--text-white);
  }
</style>
</head>
<body>
<main class="canvas">
  <svg class="label" viewBox="0 0 680 933" xmlns="http://www.w3.org/2000/svg">
    <defs>
      <clipPath id="label-shape">
        <path d="M30,0 H650 Q680,0 676,30 L552,905 Q548,933 520,933 H165 Q137,933 133,905 L4,30 Q0,0 30,0 Z"/>
      </clipPath>
      <radialGradient id="sketch-tone" cx="50%" cy="45%" r="60%">
        <stop offset="0%" stop-color="var(--sketch-lilac)" stop-opacity="0.35"/>
        <stop offset="100%" stop-color="var(--sketch-lilac)" stop-opacity="0.08"/>
      </radialGradient>
    </defs>

    <g clip-path="url(#label-shape)">
      <rect class="label-body" x="0" y="0" width="680" height="933"/>
      <rect x="55" y="298" width="530" height="552" rx="40" fill="url(#sketch-tone)"
            role="img" aria-label="Engraved line illustration of two artichoke heads on leafy stems"/>
      <rect class="label-band" x="0" y="850" width="680" height="83"/>
    </g>
    <path class="label-outline" d="M30,0 H650 Q680,0 676,30 L552,905 Q548,933 520,933 H165 Q137,933 133,905 L4,30 Q0,0 30,0 Z"/>
    <path class="label-frame" d="M142,850 L22,40 Q20,15 45,15 H635 Q660,15 658,40 L543,850"/>

    <text class="text-maker" x="345" y="49" text-anchor="middle">FABBRICA LIQUORI</text>
    <text class="text-brand" x="342" y="96" text-anchor="middle">F.LLI VERANI</text>

    <text class="text-product" transform="translate(382,813) rotate(-90)" textLength="645" lengthAdjust="spacing">CARCIOFO</text>
    <text class="text-tagline" transform="translate(289,813) rotate(-90)" textLength="525" lengthAdjust="spacing">AMARO DI CARATTERE</text>

    <text class="text-origin" x="344" y="880" text-anchor="middle">BORGO DEL MONTE</text>
    <text class="text-origin" x="344" y="907" text-anchor="middle">EST. 1886</text>
  </svg>
</main>
</body>
</html>
```